Etiketten-Design für Kräuterbonbon-Metalldose
Judith Varnholt hat sehr viel Talent. Das Design ist absolut kreativ.
Zielgruppe
Unsere Firma VelortaPharm verkauft verschiedene Sorten Kräuterbonbons.
Wir brauchen ein Etikett, dass auf eine Metall-Dose (Durchmesser 10 cam, Höhe ca. 3 cm) geklebt wird.
Zielgruppe: jung-alt
Aufgabenstellung
Der Name unserer Kräuterbonbons ist Wiesentropf.
Wir möchten, dass unsere Kunden, wenn sie das Etikett sehen einen Bezug zur Schweiz herstellen können.
Wir verwenden für unsere Bonbons unterschiedliche Kräuter für verschiedene Anwendungen:
Konkret sind erstmal 4 Dosen geplant:
-Kräutermischung aus 16 Kräuter gegen Husten
-Salbei gegen Halsschmerzen
-Anis gegen Magenschmerzen
-Zitrone/Ingwer für die Nerven
Vorderseite: Produktbeschreibung
Rückseite: unsere Herstellerangaben
Größenangaben der Dose: Durchmesser 10 cm, Höhe ca. 3 cm
Im Anhang habe ich Ihnen noch weitere/ genauere Informationen zur Verfügung bereitgestellt!

```html
<!DOCTYPE html>
<html lang="de">
<head>
<meta charset="utf-8">
<title>Wiesentropf – Zitrone/Ingwer Etikett</title>
<link rel="stylesheet" href="https://fonts.googleapis.com/css2?family=Open+Sans:wght@700;800&display=swap">
<style>
  :root {
    --brand-orange: #f7941d;
    --label-white: #ffffff;
    --pattern-light: #f1f1ef;
    --pattern-mid: #e4e6df;
    --leaf-green: #9fbf7a;
    --lemon-yellow: #f4c430;
    --ginger-tan: #cdb08a;
    --page-bg: #ffffff;
  }
  html, body {
    margin: 0;
    padding: 0;
    width: 1200px;
    height: 1200px;
    overflow: hidden;
    background: var(--page-bg);
  }
  .tin-label {
    display: block;
    width: 1200px;
    height: 1200px;
    font-family: "Open Sans", Arial, sans-serif;
  }
  .brand-name {
    font-size: 68px;
    font-weight: 800;
    fill: var(--label-white);
  }
  .origin-line {
    font-size: 38px;
    font-weight: 800;
    letter-spacing: 5px;
    fill: var(--label-white);
  }
  .variety {
    font-size: 64px;
    font-weight: 700;
    fill: var(--brand-orange);
  }
  .tab-text {
    font-weight: 700;
    fill: var(--label-white);
  }
  .tab-weight { font-size: 46px; }
  .tab-count { font-size: 48px; }
  .tab-count-unit { font-size: 24px; }
</style>
</head>
<body>
<svg class="tin-label" viewBox="0 0 1200 1200" xmlns="http://www.w3.org/2000/svg">
  <defs>
    <radialGradient id="pattern-field" cx="50%" cy="45%" r="55%">
      <stop offset="0%" stop-color="var(--pattern-light)"/>
      <stop offset="100%" stop-color="var(--pattern-mid)"/>
    </radialGradient>
    <linearGradient id="produce-tones" x1="0" y1="0" x2="1" y2="1">
      <stop offset="0%" stop-color="var(--ginger-tan)"/>
      <stop offset="45%" stop-color="var(--leaf-green)"/>
      <stop offset="100%" stop-color="var(--lemon-yellow)"/>
    </linearGradient>
    <path id="brand-arc" d="M 235 600 A 365 365 0 0 1 965 600"/>
    <path id="origin-arc" d="M 188 600 A 412 412 0 0 0 1012 600"/>
  </defs>

  <!-- label disc with herb leaf pattern -->
  <circle class="label-disc" cx="600" cy="600" r="550" fill="url(#pattern-field)"
          role="img" aria-label="Dezentes Muster aus Blättern und Kräutern"/>

  <!-- orange ring -->
  <circle class="brand-ring" cx="600" cy="600" r="388" fill="none"
          stroke="var(--brand-orange)" stroke-width="116"/>

  <!-- side tabs -->
  <rect class="side-tab side-tab-left" x="140" y="537" width="170" height="131" rx="60" fill="var(--brand-orange)"/>
  <rect class="side-tab side-tab-right" x="892" y="537" width="170" height="131" rx="60" fill="var(--brand-orange)"/>

  <!-- brand name on ring -->
  <text class="brand-name"><textPath href="#brand-arc" startOffset="50%" text-anchor="middle">Wiesentropf</textPath></text>

  <!-- herb sprig decorations beside name -->
  <rect class="sprig" x="268" y="218" width="82" height="62" rx="18" fill="var(--label-white)" opacity="0.85"
        role="img" aria-label="Kleiner Kräuterzweig"/>
  <rect class="sprig" x="850" y="218" width="82" height="62" rx="18" fill="var(--label-white)" opacity="0.85"
        role="img" aria-label="Kleiner Kräuterzweig"/>

  <!-- leaf emblem -->
  <rect class="leaf-emblem" x="560" y="264" width="90" height="140" rx="40" fill="var(--brand-orange)" opacity="0.9"
        role="img" aria-label="Stilisierter Blattzweig"/>

  <!-- variety -->
  <text class="variety" x="600" y="546" text-anchor="middle">Zitrone/Ingwer</text>
  <text class="variety" x="600" y="628" text-anchor="middle">für die Nerven</text>

  <!-- tab content -->
  <text class="tab-text tab-weight" x="222" y="619" text-anchor="middle">125G</text>
  <text class="tab-text" x="978" y="620" text-anchor="middle"><tspan class="tab-count">16</tspan><tspan class="tab-count-unit" dx="8">pieces</tspan></text>

  <!-- produce image area -->
  <path class="produce-visual" d="M 420 740 Q 470 700 560 715 Q 680 760 790 830 Q 800 930 720 975 Q 600 990 470 960 Q 400 880 420 740 Z"
        fill="url(#produce-tones)" role="img" aria-label="Foto von Ingwerwurzel, Minzblättern und Zitronen"/>

  <!-- origin line on ring -->
  <text class="origin-line"><textPath href="#origin-arc" startOffset="50%" text-anchor="middle">Schweizer Kräuterbonbon</textPath></text>
</svg>
</body>
</html>
```